Corwenna Foundation is a new grant making charity set up in the UK.

Having got a logo, we now need a website to go with it. We have worked out the text which people are going to need in order to then apply for grants. But having found out what we require they will probably need to go away and think about it.
We have to be careful of what images we use. So I have uploaded some images that we like. We are also going to be adding more pages almost immediately so need to think about the images for these.
I know basic wordpress so I will be able to add new pages/make alterations in future.
Updates
The website does need to be coded in Wordpress so that I can maintain it afterwards.
Corwenna
Brief changed to provide more money and we have also provided more possible pictures. And generally more explanation.
Target Market(s)
departments in universities, other charities doing work on relief of pain, people working in health service departments
Industry/Entity Type
Health Charity
Coding
Coded - Design and coding required
Number of Pages Required
4 page
Look and feel
Each slider illustrates characteristics of the customer's brand and the style your logo design should communicate.

```html
<!DOCTYPE html>
<html lang="en">
<head>
<meta charset="utf-8">
<title>Corwenna Foundation</title>
<link href="https://fonts.googleapis.com/css2?family=Roboto:wght@400;500;700&family=Lato:wght@400;700&display=swap" rel="stylesheet">
<style>
:root{
  --blue:#0f6fc0;
  --blue-dark:#0a5aa3;
  --ink:#222;
  --muted:#444;
  --line:#555;
  --footer:#000;
  --white:#fff;
}
*{box-sizing:border-box;margin:0;padding:0}
html,body{width:1200px;height:3223px;overflow:hidden}
body{position:relative;font-family:"Lato",sans-serif;color:var(--ink);background:var(--white)}
.abs{position:absolute}
.center{text-align:center}
.topline{left:0;top:0;width:1200px;height:4px;background:var(--blue)}
.brand{display:flex;align-items:center;gap:8px;font-family:"Roboto",sans-serif;font-weight:700;font-size:28px;color:var(--blue);letter-spacing:.3px}
.brand .mark{width:34px;height:34px;background:var(--blue)}
.header-reg{left:492px;top:31px;font-family:"Roboto",sans-serif;font-weight:500;font-size:13.5px;color:#333}
.header-social{left:730px;top:33px;display:flex;gap:14px;align-items:center}
.header-social span{width:9px;height:9px;background:#333;border-radius:2px}
.btn{display:flex;align-items:center;justify-content:center;background:var(--blue);color:var(--white);font-family:"Roboto",sans-serif;font-weight:700;border-radius:3px}
.nav{left:133px;top:85px;width:935px;height:50px;background:var(--blue);display:flex;justify-content:center;gap:36px;align-items:center;z-index:2}
.nav a{color:var(--white);text-decoration:none;font-family:"Roboto",sans-serif;font-weight:700;font-size:13.5px}
.hero{left:0;top:113px;width:1200px;height:600px;background:radial-gradient(ellipse at 32% 25%,#c58a3a 0,#6a4a2a 10%,transparent 24%),radial-gradient(ellipse at 78% 70%,#b07a3a 0,transparent 18%),radial-gradient(ellipse at 55% 45%,#3a6da0 0,#1b3a60 35%,#0b1a30 75%)}
.hero h1{left:0;top:300px;width:1200px;font-family:"Roboto",sans-serif;font-weight:700;font-size:41px;line-height:50px;color:var(--white)}
.hero p{left:0;top:420px;width:1200px;font-size:13.5px;color:var(--white)}
.dots{left:578px;top:656px;display:flex;gap:3px}
.dots span{width:9px;height:9px;border-radius:50%;background:var(--white)}
.dots span:first-child{background:var(--blue)}
.section-title{left:0;width:1200px;font-family:"Roboto",sans-serif;font-weight:700;font-size:33px;color:var(--blue)}
.bar{left:585px;width:30px;height:5px;background:var(--blue)}
.lead{left:0;width:1200px;font-size:13.5px;line-height:28px;color:var(--muted)}
.card{background:var(--white);box-shadow:0 0 10px rgba(0,0,0,.12);text-align:center;padding:18px 14px 0}
.card .icon{width:86px;height:86px;border-radius:50%;background:var(--blue);margin:0 auto 14px;display:flex;align-items:center;justify-content:center}
.card h3{font-family:"Roboto",sans-serif;font-weight:500;font-size:15.5px;line-height:28px;color:#222;margin-bottom:10px}
.card p{font-size:13px;line-height:28px;color:var(--muted)}
.grants-bg{left:0;top:1690px;width:1200px;height:585px;background:linear-gradient(100deg,#1a6fc0 0%,#1b7ccc 50%,#2a8ad6 100%)}
.grants .white{color:var(--white)}
.grant-item{top:1963px;width:190px;text-align:center}
.grant-item .ring{width:96px;height:96px;border-radius:50%;background:var(--white);margin:0 auto 16px;display:flex;align-items:center;justify-content:center}
.grant-item span{font-family:"Roboto",sans-serif;font-weight:700;font-size:13px;line-height:28px;color:var(--white)}
.field{border:1px solid #555;font-size:12px;color:#333;padding:22px 11px 0;font-family:"Lato",sans-serif;background:var(--white)}
.footer{left:0;top:2864px;width:1200px;height:359px;background:var(--footer);color:var(--white)}
.footer h4{font-family:"Roboto",sans-serif;font-weight:700;font-size:15.5px}
.footer ul{list-style:none;font-size:14px;line-height:28px}
.footer li::before{content:"»";margin-right:10px}
.contact-row{display:flex;gap:14px;align-items:flex-start;font-size:14px;line-height:28px}
.contact-row .ic{flex:none;width:30px;height:30px;border-radius:50%;background:var(--blue);display:flex;align-items:center;justify-content:center;margin-top:-2px}
.social-dot{width:30px;height:30px;border-radius:50%;background:var(--blue)}
.copy{font-size:12.5px}
</style>
</head>
<body>
<div class="abs topline"></div>

<header>
  <div class="abs brand" style="left:133px;top:26px"><span class="mark"></span>CORWENNA</div>
  <div class="abs header-reg">Charity registration No : &nbsp;1187305</div>
  <div class="abs header-social"><span></span><span></span><span></span><span></span></div>
  <a class="abs btn" style="left:888px;top:19px;width:178px;height:44px;font-size:15.5px;text-decoration:none">GET IN TOUCH</a>
  <nav class="abs nav"><a href="#">HOME</a><a href="#">ABOUT US</a><a href="#">GRANTS</a><a href="#">CONTACT US</a></nav>
</header>

<section class="hero-wrap">
  <div class="abs hero" role="img" aria-label="Close-up of glowing nerve cells in blue and amber light"></div>
  <h1 class="abs center" style="left:0;top:305px;width:1200px;font-family:'Roboto',sans-serif;font-weight:700;font-size:41px;line-height:50px;color:#fff">CORWENNA FOUNDATION IS A GRANT MAKING<br>CHARITY SET UP IN THE UK IN 2021</h1>
  <p class="abs center" style="left:0;top:420px;width:1200px;font-size:13.5px;color:#fff">The main aim of Corwenna Foundation is to reduce the suffering caused by chronic pain.</p>
  <div class="abs btn" style="left:422px;top:467px;width:355px;height:42px;font-size:16px">CHARITY REGISTRATION NUMBER : 1187305</div>
  <div class="abs dots"><span></span><span></span><span></span><span></span></div>
</section>

<section class="about">
  <h2 class="abs section-title center" style="top:784px">ABOUT CORWENNA FOUNDATION</h2>
  <div class="abs bar" style="top:830px"></div>
  <p class="abs lead center" style="top:853px">Lorem ipsum dolor sit amet, consectetur adipiscing elit, sed do eiusmod tempor incididunt ut labore et dolore magna aliqua.<br>Quis ipsum suspendisse ultrices gravida. Risus commodo viverra maecenas accumsan lacus vel facilisis.</p>

  <article class="abs card" style="left:131px;top:940px;width:297px;height:284px">
    <div class="icon"><svg width="50" height="40" viewBox="0 0 50 40" fill="none" stroke="#fff" stroke-width="2"><path d="M2 12l10-6 8 4 6-3 8 3 14-2"/><path d="M12 24l8 8 4-2 4 4 4-3 4 2 6-6"/><path d="M20 14l8 6"/></svg></div>
    <h3>WHO ARE THE TRUSTEES OF<br>CORWENNA FOUNDATION?</h3>
    <p>The initial trustees are Corwenna, Tomas &amp; Elwin Pellowe.A fourth trustee is about to be ap-pointed, the legal firm of Harcourt Lane.</p>
  </article>
  <article class="abs card" style="left:452px;top:940px;width:296px;height:284px">
    <div class="icon"><svg width="46" height="44" viewBox="0 0 46 44" fill="none" stroke="#fff" stroke-width="2"><rect x="3" y="6" width="40" height="28" rx="2"/><circle cx="23" cy="16" r="5"/><path d="M14 32c2-6 16-6 18 0M18 40h10M23 34v6"/></svg></div>
    <h3>WHO ARE THE MEDICAL ADVISERS<br>TO CORWENNA FOUNDATION?</h3>
    <p>The medical advisers are doctors or other health professionals, who individually or col-lectively advise the trustees.</p>
  </article>
  <article class="abs card" style="left:772px;top:940px;width:297px;height:284px">
    <div class="icon"><svg width="46" height="44" viewBox="0 0 46 44" fill="none" stroke="#fff" stroke-width="2"><circle cx="26" cy="13" r="9"/><path d="M26 8v10M4 30l10-4h12l-2 4h-8M4 40l8-4h14l14-10"/></svg></div>
    <h3>HOW MUCH MONEY DOES<br>CORWENNA FOUNDATION HAVE?</h3>
    <p>It is unclear how much money the Foundation will have in a few years time, but currently it has about a million pounds.</p>
  </article>
  <article class="abs card" style="left:133px;top:1253px;width:455px;height:332px">
    <div class="icon"><svg width="46" height="46" viewBox="0 0 46 46" fill="none" stroke="#fff" stroke-width="2"><path d="M26 10c-6 4-10 10-10 18 0 8 6 12 13 12s13-4 13-12c0-8-5-14-10-18z"/><path d="M24 6h10l-2 4h-6z"/><rect x="4" y="28" width="10" height="14"/><rect x="8" y="20" width="8" height="8"/></svg></div>
    <h3>WHERE HAS THIS MONEY<br>COME FROM?</h3>
    <p>The million pounds has been inherited from Corwenna's father, the<br>late Sir Gerald Ashworth, who had a large stake in the Ashworth<br>supermarket business. Further significant money is going to come<br>from the sale of the farm where the Pellowe family currently live.</p>
  </article>
  <article class="abs card" style="left:612px;top:1253px;width:455px;height:339px">
    <div class="icon"><svg width="40" height="52" viewBox="0 0 40 52" fill="none" stroke="#fff" stroke-width="4"><path d="M8 14a12 12 0 1 1 18 10c-5 3-6 6-6 10v4"/><circle cx="20" cy="46" r="3"/></svg></div>
    <h3>WHY IS THE FOUNDATION NAMED AFTER<br>CORWENNA PELLOWE?</h3>
    <p>Corwenna Pellowe suffered from extreme pain for many years after a suc-cessful operation to cure her cancer of the tongue. Although the pain is now well controlled, the family would like the unexpected receipt of such a large amount of money from the farm, to help prevent other people going through such a difficult time.</p>
  </article>
</section>

<section class="grants">
  <div class="abs grants-bg" role="img" aria-label="Blue scientific background with a gloved hand and molecular diagrams"></div>
  <h2 class="abs section-title center white" style="top:1745px;color:#fff">GRANTS</h2>
  <div class="abs bar" style="top:1788px;background:#fff"></div>
  <p class="abs lead center" style="top:1805px;color:#fff">Grants will almost entirely be provided for research or education into pain management, or the prevention of pain.<br>The trustees will also be providing grants to a number of other charities or to areas with which they have had a long term as-<br>sociation, such as HIV/AIDS and TB. There is no application procedure for these other areas, and unsolicited applications are<br>unlikely to be favorably considered by the trustees.</p>

  <div class="abs grant-item" style="left:30px"><div class="ring"><svg width="50" height="56" viewBox="0 0 50 56" fill="none" stroke="#0f6fc0" stroke-width="2"><path d="M10 4c-4 10-6 30 0 48h30c6-18 4-38 0-48"/><path d="M25 8v40M19 26c-3 2-3 6 0 8M31 26c3 2 3 6 0 8"/></svg></div><span>PAIN CENTRES</span></div>
  <div class="abs grant-item" style="left:210px"><div class="ring"><svg width="40" height="56" viewBox="0 0 40 56" fill="none" stroke="#0f6fc0" stroke-width="2.5"><rect x="10" y="2" width="20" height="8"/><rect x="5" y="14" width="30" height="40" rx="3"/><path d="M20 26v14M13 33h14"/></svg></div><span>THE USE OF OPIOIDS</span></div>
  <div class="abs grant-item" style="left:405px"><div class="ring"><svg width="56" height="46" viewBox="0 0 56 46" fill="none" stroke="#0f6fc0" stroke-width="2.5"><rect x="4" y="10" width="48" height="32" rx="4"/><path d="M20 10V4h16v6M24 18h8v6h6v8h-6v6h-8v-6h-6v-8h6z"/></svg></div><span>IMPROVING THE USE<br>OF MEDICATION</span></div>
  <div class="abs grant-item" style="left:583px"><div class="ring"><svg width="56" height="48" viewBox="0 0 56 48" fill="none" stroke="#0f6fc0" stroke-width="2.5"><rect x="8" y="10" width="40" height="28"/><path d="M2 42h52M18 18l10-5 10 5-10 5zM22 20v6c4 3 8 3 12 0v-6"/></svg></div><span>EDUCATION</span></div>
  <div class="abs grant-item" style="left:763px"><div class="ring"><svg width="56" height="50" viewBox="0 0 56 50" fill="none" stroke="#0f6fc0" stroke-width="2.5"><path d="M14 4v18M20 2v20M26 4v18M8 10v16c0 8 6 12 14 12h10l18-12"/><circle cx="22" cy="38" r="4"/></svg></div><span>IMPROVED TYPES OF<br>PAIN CONTROL</span></div>
  <div class="abs grant-item" style="left:962px"><div class="ring"><svg width="56" height="52" viewBox="0 0 56 52" fill="none" stroke="#0f6fc0" stroke-width="2.5"><ellipse cx="24" cy="16" rx="18" ry="10"/><path d="M6 16v10c0 6 8 10 18 10M42 16v10L26 46h20M12 30v4M18 33v4M24 36v4"/></svg></div><span>MEASURING PAIN</span></div>

  <p class="abs lead center" style="top:2142px;color:#fff">The trustees will initially consider unsolicited applications, for up to £50,000 each, in these areas or related areas. Applica-<br>tions for more substantial project funding will be invited in due course.</p>
</section>

<section class="contact">
  <h2 class="abs section-title center" style="top:2345px">GET IN TOUCH</h2>
  <div class="abs bar" style="top:2392px"></div>
  <p class="abs lead center" style="top:2415px">Lorem ipsum dolor sit amet, consectetur adipiscing elit, sed do eiusmod tempor incididunt ut labore et dolore magna aliqua.<br>Quis ipsum suspendisse ultrices gravida. Risus commodo viverra maecenas accumsan lacus vel facilisis.</p>
  <form>
    <div class="abs field" style="left:168px;top:2491px;width:424px;height:54px">First Name</div>
    <div class="abs field" style="left:608px;top:2491px;width:423px;height:54px">Last Name</div>
    <div class="abs field" style="left:168px;top:2559px;width:424px;height:54px">Phone Number</div>
    <div class="abs field" style="left:608px;top:2559px;width:423px;height:54px">Email Address</div>
    <div class="abs field" style="left:168px;top:2628px;width:863px;height:117px">Message</div>
    <div class="abs btn" style="left:494px;top:2765px;width:212px;height:44px;font-size:15.5px">SUMBIT</div>
  </form>
</section>

<footer class="abs footer">
  <div class="abs brand" style="left:135px;top:147px;color:#fff"><span class="mark" style="background:#fff"></span>CORWENNA</div>
  <div class="abs" style="left:145px;top:209px;display:flex;gap:19px"><span class="social-dot"></span><span class="social-dot"></span><span class="social-dot"></span><span class="social-dot"></span></div>

  <h4 class="abs" style="left:408px;top:69px">QUICK LINKS</h4>
  <ul class="abs" style="left:400px;top:99px"><li>Home</li><li>About Us</li><li>Grants</li><li>Contact Us</li></ul>

  <h4 class="abs" style="left:609px;top:69px">IMPORTANCE</h4>
  <ul class="abs" style="left:597px;top:99px"><li>Privacy Policy</li><li>Sitemap</li><li>COVID-19 Update</li><li>Careers</li></ul>

  <h4 class="abs" style="left:816px;top:69px">CONTACT INFO</h4>
  <div class="abs" style="left:806px;top:102px;width:290px;display:flex;flex-direction:column;gap:18px">
    <div class="contact-row"><span class="ic"><svg width="12" height="16" viewBox="0 0 12 16"><path d="M6 0a6 6 0 0 0-6 6c0 4 6 10 6 10s6-6 6-10a6 6 0 0 0-6-6z" fill="#fff"/><circle cx="6" cy="6" r="2" fill="#0f6fc0"/></svg></span><span>123 Lorem ipsum dolor sit amet con<br>sectetur adipiscing elit .</span></div>
    <div class="contact-row"><span class="ic"><svg width="14" height="14" viewBox="0 0 14 14"><path d="M3 0l3 3-2 2c1 2 3 4 5 5l2-2 3 3-2 3C6 14 0 8 0 2z" fill="#fff"/></svg></span><span>888 8888 888</span></div>
    <div class="contact-row"><span class="ic"><svg width="14" height="10" viewBox="0 0 14 10"><rect width="14" height="10" fill="#fff"/><path d="M0 0l7 6 7-6" fill="none" stroke="#0f6fc0" stroke-width="1.5"/></svg></span><span>info@corwennafoundation.org</span></div>
  </div>

  <div class="abs" style="left:118px;top:287px;width:961px;height:1px;background:#666"></div>
  <p class="abs copy" style="left:135px;top:303px">© Copyrights 2021 Corwenna Foundation &nbsp;&nbsp;| &nbsp;&nbsp;All Rights Reserved</p>
  <p class="abs copy" style="left:864px;top:303px">Privacy policy &nbsp;&nbsp;| &nbsp;&nbsp;Terms of Service</p>
</footer>
</body>
</html>
```